Mirelo Japanese Restaurant

We just want the japanese sakura background and the menu as below

Side dish :
Edamame $4
Japanese Steam Green Bean
Crab Craw $3 each
With Japanese mayo
Teriyaki Chicken stick $3 each
Chicken stick with home made teriyaki sauce
Tempura Prawns $7
With Japanese mayo
Miso Soup $3
Traditional Japanese soup
Salt and Pepper Calamari $7
With japanese mayo

Main dish:
Gyu Don $12
Bowl of steam rice topped with beef and onion simmered in a mildly sweet sauce.
Teriyaki Don $12
Bowl of steam rice topped with your choice of beef, chicken or pork and with our special Teriyaki sauce.
Vege Don $12
Bowl of steam rice with seasonal Vegetables with the special japanese sweet soy sauce.
Japanese Curry $12,(prawns $14)
Bowl of steam rice with Chicken, pork or prawn with japanese mild curry sauce.
Katsu Don $12
Bowl of steam rice topped with a deep-fried pork cutlet and egg with the japanese special sauce.
Oyako Don $12
Bowl of steam rice topped with chick and egg with japanese special sauce.
Spice Don $12
Bowl of steam rice topped with beef or chicken with japanese spice sauce.
Gingle Don $12
Bowl of steam rice topped with beef or chicken with japanese ginger sauce.
Sushi $3
Roll everyday on seasonal
ingredient.

Japanese-style sweets
Black Sesame Ice cream $4.5
Green tea Ice cream $4.5

Restaurant

```html
<!DOCTYPE html>
<html lang="en">
<head>
<meta charset="utf-8">
<title>Mirelo Japanese Restaurant – Menu</title>
<link rel="stylesheet" href="https://fonts.googleapis.com/css2?family=Kaushan+Script&family=Libre+Baskerville:wght@400&display=swap">
<style>
  :root {
    --canvas: #ffffff;
    --panel: #fce9e8;
    --cover: #f4d9d6;
    --blossom: #f0657a;
    --bark: #231f20;
    --ink: #1a1a1a;
    --band: #fbeff0;
    --band-edge: #8a8a8a;
    --tree-faint: rgba(180, 170, 170, 0.35);
  }
  * { box-sizing: border-box; margin: 0; padding: 0; }
  html, body { width: 939px; height: 1200px; overflow: hidden; background: var(--canvas); }
  body { position: relative; font-family: "Libre Baskerville", Georgia, serif; color: var(--ink); }

  .panel { position: absolute; width: 418px; overflow: hidden; background: var(--panel); }
  .panel--cover { left: 0; top: 0; height: 589px; background: var(--cover); }
  .panel--sides { left: 521px; top: 0; height: 589px; }
  .panel--mains { left: 0; top: 608px; height: 592px; }
  .panel--sweets { left: 521px; top: 608px; height: 592px; }

  .cover-art {
    position: absolute; inset: 0;
    background:
      radial-gradient(circle at 60% 20%, rgba(240,101,122,0.55), transparent 45%),
      radial-gradient(circle at 45% 80%, rgba(240,101,122,0.45), transparent 40%),
      linear-gradient(180deg, #fbe4e6 0%, #f4d9d6 100%);
  }
  .tree-watermark {
    position: absolute; left: 60px; top: 40px; width: 300px; bottom: 0;
    background: radial-gradient(ellipse at 50% 40%, var(--tree-faint), transparent 70%);
  }

  .title-band {
    position: absolute; left: 0; top: 240px; width: 418px; height: 110px;
    background: var(--band); border-top: 1px solid var(--band-edge); border-bottom: 1px solid var(--band-edge);
  }
  .title-band__mark {
    position: absolute; left: 14px; top: 14px; width: 64px; height: 80px;
    border-radius: 50%; background: #ffffff; border: 2px solid #c9c0c0;
  }
  .title-band__name {
    position: absolute; left: 92px; top: 12px; width: 230px;
    font-family: "Kaushan Script", cursive; color: var(--bark); text-align: center; line-height: 1.15;
  }
  .title-band__name .big { display: block; font-size: 34px; letter-spacing: 2px; }
  .title-band__name .small { display: block; font-size: 22px; margin-top: 8px; }
  .title-band__art {
    position: absolute; right: 6px; top: 4px; width: 84px; height: 100px;
    background: linear-gradient(180deg, #f3eeee, #d8d2d2);
  }

  .menu-heading {
    position: absolute; font-family: "Kaushan Script", cursive; font-weight: 400; color: var(--bark);
    text-align: center; line-height: 1;
  }
  .menu-list { position: absolute; list-style: none; }
  .menu-item { margin-bottom: 15px; }
  .menu-item__line { display: flex; align-items: baseline; font-size: 15px; }
  .menu-item__leader { flex: 1; border-bottom: 2px dotted var(--ink); margin: 0 2px 4px; }
  .menu-item__desc { font-size: 11.5px; line-height: 1.4; margin-left: 2px; }
</style>
</head>
<body>

<section class="panel panel--cover">
  <div class="cover-art" role="img" aria-label="Cherry blossom tree with dark branches and pink petals"></div>
  <div class="title-band">
    <div class="title-band__mark"></div>
    <h1 class="title-band__name"><span class="big">MIRELO</span><span class="small">Japanese Restaurant</span></h1>
    <div class="title-band__art" role="img" aria-label="Small ink painting of a blossom tree and mountain"></div>
  </div>
</section>

<section class="panel panel--sides">
  <div class="tree-watermark" role="img" aria-label="Faint cherry blossom tree in the background"></div>
  <h2 class="menu-heading" style="left:0;width:342px;top:8px;font-size:48px;">Side Dish</h2>
  <ul class="menu-list" style="left:27px;top:66px;width:288px;">
    <li class="menu-item"><div class="menu-item__line"><span>Edamame</span><span class="menu-item__leader"></span><span>$4</span></div><p class="menu-item__desc">(Japanese steam green bean)</p></li>
    <li class="menu-item"><div class="menu-item__line"><span>Crab Claw</span><span class="menu-item__leader"></span><span>$3</span></div><p class="menu-item__desc">(with Japanese mayo)</p></li>
    <li class="menu-item"><div class="menu-item__line"><span>Tempura Prawns</span><span class="menu-item__leader"></span><span>$7</span></div><p class="menu-item__desc">(with Japanese mayo)</p></li>
    <li class="menu-item"><div class="menu-item__line"><span>Miso Soup</span><span class="menu-item__leader"></span><span>$3</span></div><p class="menu-item__desc">(Traditional Japanese Soup)</p></li>
    <li class="menu-item"><div class="menu-item__line"><span>Salt &amp; Pepper Calamari</span><span class="menu-item__leader"></span><span>$7</span></div><p class="menu-item__desc">(with Japanese mayo)</p></li>
  </ul>
  <h2 class="menu-heading" style="left:0;width:330px;top:308px;font-size:48px;">Main Dish</h2>
  <ul class="menu-list" style="left:27px;top:366px;width:288px;">
    <li class="menu-item" style="margin-bottom:18px;"><div class="menu-item__line"><span>GyuDon</span><span class="menu-item__leader"></span><span>$12</span></div><p class="menu-item__desc">(bowl of steamed rice toped with beef<br>&amp; onion simmered in a mildly sweet<br>sauce)</p></li>
    <li class="menu-item"><div class="menu-item__line"><span>TeriyakiDon</span><span class="menu-item__leader"></span><span>$12</span></div><p class="menu-item__desc">(bowl of steamed rice topped with your<br>choice of beef, chicken or pork &amp; with<br>our special teriyaki sauce)</p></li>
  </ul>
</section>

<section class="panel panel--mains">
  <div class="tree-watermark" role="img" aria-label="Faint cherry blossom tree in the background"></div>
  <ul class="menu-list" style="left:18px;top:60px;width:306px;">
    <li class="menu-item" style="margin-bottom:12px;">
      <div class="menu-item__line"><span>Japanese curry</span><span class="menu-item__leader"></span><span>$12</span></div>
      <div class="menu-item__line"><span>with prawn</span><span class="menu-item__leader"></span><span>$14</span></div>
      <p class="menu-item__desc">(bowl of steamed rice with chicken,<br>pork or prawn with Japanese mild<br>curry sauce)</p></li>
    <li class="menu-item" style="margin-bottom:22px;"><div class="menu-item__line"><span>KatsuDon</span><span class="menu-item__leader"></span><span>$12</span></div><p class="menu-item__desc">(bowl of steamed rice topped with<br>a deep-fried pork cutlet and egg<br>with Japanese special sauce)</p></li>
    <li class="menu-item" style="margin-bottom:22px;margin-left:5px;"><div class="menu-item__line"><span>OyakoDon</span><span class="menu-item__leader"></span><span>$12</span></div><p class="menu-item__desc">(bowl of steamed rice topped with<br>chicken and egg with Japanese<br>special sauce)</p></li>
    <li class="menu-item" style="margin-bottom:22px;margin-left:5px;"><div class="menu-item__line"><span>SpiceDon</span><span class="menu-item__leader"></span><span>$12</span></div><p class="menu-item__desc">(bowl of steamed rice topped with<br>beef or chicken with Japanese<br>spice sauce)</p></li>
    <li class="menu-item" style="margin-bottom:26px;margin-left:5px;"><div class="menu-item__line"><span>GingleDon</span><span class="menu-item__leader"></span><span>$12</span></div><p class="menu-item__desc">(bowl of steamed rice topped with<br>beef or chicken with Japanese<br>ginger sauce)</p></li>
    <li class="menu-item" style="margin-left:5px;"><div class="menu-item__line"><span>Sushi</span><span class="menu-item__leader"></span><span>$3</span></div><p class="menu-item__desc">(Roll everyday on seasonal<br>ingredients)</p></li>
  </ul>
</section>

<section class="panel panel--sweets">
  <div class="tree-watermark" role="img" aria-label="Faint cherry blossom tree in the background"></div>
  <h2 class="menu-heading" style="left:-2px;width:424px;top:18px;font-size:50px;">Japanese Sweets</h2>
  <ul class="menu-list" style="left:19px;top:122px;width:328px;">
    <li class="menu-item" style="margin-bottom:16px;"><div class="menu-item__line"><span>Black Sesame Ice cream</span><span class="menu-item__leader"></span><span>$4.5</span></div></li>
    <li class="menu-item"><div class="menu-item__line"><span>Green Tea Ice cream</span><span class="menu-item__leader"></span><span>$4.5</span></div></li>
  </ul>
</section>

</body>
</html>
```